Wandrift: Travel business card redesign

We need a clean elegant look for our cards featuring blue and orange. Look should communicate a sense of strong design and seem uncluttered. The company is Wandrift which means drift to wander. As in every trip is an drift to wander. Feel free to reinvent the logo or just tweak it. Colors should be blue like Caribbean waters and a saturated orange. Keep it clean and simple.
Please match the information in the sample uploaded but the sample is horrible -- a non-starter -- use for information only. also please add managing director to my name as title

Target Market(s)
potential clients, hotels, trade publications
Industry/Entity Type
Travel Industry
Contact Information for Business Card
as above
Requirements
Must have
- Font should be century gothic. Colors below are close but a but prefer lighter in each case.

```html
<!DOCTYPE html>
<html lang="en">
<head>
<meta charset="utf-8">
<title>Wandrift business cards</title>
<link rel="stylesheet" href="https://fonts.googleapis.com/css2?family=Mulish:wght@800&family=Questrial&display=swap">
<style>
  :root {
    --page: #e9e7e3;
    --ink-dark: #0d0e10;
    --ink-dark-2: #1b1d21;
    --paper: #f4f4f4;
    --orange: #f47a2a;
    --blue: #2a9fdc;
    --blue-soft: #3aa8e6;
    --ghost: rgba(255,255,255,0.05);
    --shadow: 0 18px 40px rgba(0,0,0,0.28);
  }
  * { box-sizing: border-box; margin: 0; padding: 0; }
  html, body { width: 1200px; height: 784px; overflow: hidden; }
  body {
    background: var(--page);
    position: relative;
    font-family: "Questrial", "Century Gothic", sans-serif;
  }
  .card {
    position: absolute;
    width: 640px;
    height: 366px;
    border-radius: 4px;
    overflow: hidden;
    box-shadow: var(--shadow);
  }

  /* Front card */
  .card--front {
    left: 70px; top: 36px;
    background: radial-gradient(ellipse at 50% 40%, var(--ink-dark-2), var(--ink-dark) 75%);
  }
  .card--front .texture {
    position: absolute; inset: 0;
    background: linear-gradient(160deg, rgba(255,255,255,0.03), rgba(0,0,0,0.2));
  }
  .ghost-name {
    position: absolute; left: -30px; top: 58px;
    font-family: "Mulish", sans-serif; font-weight: 800;
    font-size: 170px; letter-spacing: -4px;
    color: var(--ghost); white-space: nowrap;
  }
  .brand { position: absolute; line-height: 1; }
  .brand__name {
    font-family: "Mulish", sans-serif; font-weight: 800;
    color: var(--orange); letter-spacing: -1px;
  }
  .brand__tagline {
    display: block; color: var(--blue); text-align: right;
    font-family: "Questrial", sans-serif;
  }
  .card--front .brand { left: 150px; top: 110px; }
  .card--front .brand__name { font-size: 68px; }
  .card--front .brand__tagline { font-size: 26px; margin-top: 2px; }
  .motto {
    position: absolute; left: 30px; right: 30px; bottom: 52px;
    font-size: 17px; letter-spacing: 11px; text-align: center; white-space: nowrap;
  }
  .motto__lead { color: var(--orange); }
  .motto__rest { color: var(--blue); }

  /* Back card */
  .card--back {
    left: 500px; top: 400px;
    background: var(--ink-dark);
  }
  .card--back .upper {
    position: absolute; left: 0; top: 0; right: 0; height: 196px;
    background: linear-gradient(180deg, #ffffff, var(--paper));
  }
  .card--back .band-orange {
    position: absolute; left: 0; right: 0; top: 196px; height: 8px; background: var(--orange);
  }
  .card--back .band-blue {
    position: absolute; left: 0; right: 0; top: 204px; height: 5px; background: var(--blue);
  }
  .card--back .lower {
    position: absolute; left: 0; right: 0; top: 209px; bottom: 0;
    background: radial-gradient(ellipse at 40% 30%, var(--ink-dark-2), var(--ink-dark) 80%);
  }
  .person { position: absolute; right: 26px; top: 20px; text-align: right; }
  .person__name { color: var(--orange); font-size: 19px; }
  .person__title { color: var(--blue); font-size: 12px; margin-top: 2px; }
  .card--back .brand { left: 40px; top: 88px; }
  .card--back .brand__name { font-size: 62px; }
  .card--back .brand__tagline { font-size: 24px; margin-top: 2px; }

  .contact {
    position: absolute; left: 40px; top: 224px;
    list-style: none; color: var(--blue-soft); font-size: 17px;
  }
  .contact li { display: flex; align-items: flex-start; gap: 10px; line-height: 22px; }
  .contact svg { width: 18px; height: 18px; margin-top: 2px; flex: none; }
  .contact .address { margin-top: 12px; }
</style>
</head>
<body>

  <section class="card card--front" aria-label="Card front">
    <div class="texture" role="img" aria-label="Fine dark dotted texture"></div>
    <div class="ghost-name" aria-hidden="true">wandrift</div>
    <div class="brand">
      <div class="brand__name">wandrift</div>
      <span class="brand__tagline">drift to wander</span>
    </div>
    <p class="motto"><span class="motto__lead">a new way </span><span class="motto__rest">to see the world</span></p>
  </section>

  <section class="card card--back" aria-label="Card back">
    <div class="upper"></div>
    <div class="band-orange"></div>
    <div class="band-blue"></div>
    <div class="lower" role="img" aria-label="Fine dark dotted texture"></div>

    <div class="person">
      <div class="person__name">Lena Marsh</div>
      <div class="person__title">Managing Director</div>
    </div>

    <div class="brand">
      <div class="brand__name">wandrift</div>
      <span class="brand__tagline">drift to wander</span>
    </div>

    <ul class="contact">
      <li>
        <svg viewBox="0 0 20 20" aria-hidden="true"><path d="M5 2l3 1 1 4-2 1.5a10 10 0 0 0 4.5 4.5L13 11l4 1 1 3-2 3C8 18 2 12 2 4z" fill="#f47a2a"/></svg>
        <span>877.55 DRIFT (374386)</span>
      </li>
      <li>
        <svg viewBox="0 0 20 20" aria-hidden="true"><rect x="5" y="1.5" width="10" height="17" rx="2" fill="#f47a2a"/><rect x="7" y="4" width="6" height="9" fill="#0d0e10"/><circle cx="10" cy="15.8" r="1" fill="#0d0e10"/></svg>
        <span>323.555.0142</span>
      </li>
      <li>
        <svg viewBox="0 0 20 20" aria-hidden="true"><rect x="2" y="8" width="16" height="9" rx="1.5" fill="#f47a2a"/><rect x="5" y="3" width="10" height="6" fill="#f47a2a"/><rect x="6.5" y="4.5" width="7" height="1.2" fill="#0d0e10"/><rect x="5" y="11" width="10" height="1.5" fill="#0d0e10"/></svg>
        <span>310.555.0187</span>
      </li>
      <li class="address">
        <svg viewBox="0 0 20 20" aria-hidden="true"><path d="M10 2L1.5 10h2.5v8h4.5v-5h3v5H16v-8h2.5z" fill="#f47a2a"/></svg>
        <span>1460 Harbor Crest Way N.<br>Seaview, 90521</span>
      </li>
    </ul>
  </section>

</body>
</html>
```